Simple and Approachable Cover for Pet Expo Company Page

Size: 2000 x 430; looking simply for words "Dunmore HR Consulting" and email address "DunmoreHRConsulting@brelvamail.com." This is for a cover photo for a company profile page for the Hollow Oak Expo, where I am a featured speaker on Employee Communications later this month. You can incorporate the attached photo to the left of the banner ad if you wish. The mood I wish to present is approachable, positive and simple.

Target Market(s)

small pet retail business owners

Industry/Entity Type

Pet Shop

Font styles to use
Serif
Sans Serif

Requirements
Must have
• Email address clearly defined/separated. Easy to read.
Nice to have
• I like the picture that I included; subtle pet paw background is also nice
Should not have
• No paid stock images

```html
<!DOCTYPE html>
<html lang="en">
<head>
<meta charset="utf-8">
<title>Dunmore HR Consulting – Cover Banner</title>
<link href="https://fonts.googleapis.com/css2?family=Montserrat:wght@600;700&family=Oswald:wght@400&display=swap" rel="stylesheet">
<style>
  :root {
    --brand-blue: #1b75bb;
    --brand-orange: #f0912f;
    --ink: #111111;
    --white: #ffffff;
    --photo-light: #b9b9b9;
    --photo-mid: #8a8a8a;
    --photo-dark: #4a4a4a;
  }
  html, body {
    margin: 0;
    padding: 0;
    overflow: hidden;
    background: var(--white);
  }
  .banner {
    position: relative;
    width: 1200px;
    height: 258px;
    overflow: hidden;
  }
  .banner-shapes {
    position: absolute;
    inset: 0;
    display: block;
  }
  .brand-name {
    position: absolute;
    left: 780px;
    width: 400px;
    top: 36px;
    margin: 0;
    text-align: center;
    color: var(--white);
    font-family: "Montserrat", Arial, sans-serif;
    font-weight: 700;
    font-size: 54px;
    line-height: 1;
    letter-spacing: 6px;
  }
  .brand-tagline {
    position: absolute;
    left: 780px;
    width: 400px;
    top: 102px;
    margin: 0;
    text-align: center;
    color: var(--white);
    font-family: "Oswald", "Arial Narrow", sans-serif;
    font-weight: 400;
    font-size: 48px;
    line-height: 1;
    letter-spacing: 4px;
  }
  .contact-email {
    position: absolute;
    left: 700px;
    width: 500px;
    top: 213px;
    margin: 0;
    text-align: center;
    color: var(--ink);
    font-family: "Montserrat", Arial, sans-serif;
    font-weight: 600;
    font-size: 18px;
    line-height: 1;
    letter-spacing: 0.2px;
  }
</style>
</head>
<body>
  <header class="banner">
    <svg class="banner-shapes" width="1200" height="258" viewBox="0 0 1200 258" aria-hidden="false">
      <defs>
        <linearGradient id="portrait-tones" x1="0" y1="0" x2="1" y2="1">
          <stop offset="0" stop-color="var(--photo-dark)"/>
          <stop offset="0.45" stop-color="var(--photo-mid)"/>
          <stop offset="1" stop-color="var(--photo-light)"/>
        </linearGradient>
      </defs>
      <rect class="portrait-area" x="0" y="0" width="800" height="258" fill="url(#portrait-tones)"
            role="img" aria-label="Black and white outdoor portrait of a smiling man and woman with their dog in front of trees"/>
      <polygon class="corner-blue" points="0,0 176,0 10,258 0,258" fill="var(--brand-blue)"/>
      <polygon class="corner-stripe" points="176,0 192,0 26,258 10,258" fill="var(--brand-orange)"/>
      <polygon class="title-panel" points="790,0 1200,0 1200,258 640,258" fill="var(--brand-blue)"/>
      <polygon class="email-band" points="700,192 1200,192 1200,258 660,258" fill="var(--brand-orange)"/>
    </svg>
    <h1 class="brand-name">DUNMORE</h1>
    <p class="brand-tagline">HR Consulting</p>
    <p class="contact-email">DunmoreHRConsulting@brelvamail.com</p>
  </header>
</body>
</html>
```